Business card for communications

Need a business card for my consulting business - I work with not for profits, start ups and social enterprises on their media, communications campaigns.

Please see my website for colours, images and fonts www.morelbratton.example

Dana Morelbrat
Communications & Campaign strategist
Sydney - Melbourne
M: 0498 317 026
E: dana@morelbratton.example
S: danamorelbrat
W: morelbratton.example
T: @danamorelbrat

(above is info only and can be presented any way e.g. should not have to be M for mobile - it should be an icon)
Updates

Dear designers I have updated the brief and uploaded high res images from my website for you to use. The designs so far with the use of images and icons are much better so far. Thank you I look forward to receiving your revised designs. Dana Morelbrat

Industry/Entity Type

Communications

Font styles to use
Sans Serif

Requirements
Must have
• Icons for contact details
Images from the website www.morelbratton.example
Nice to have
• Images - attached

```html
<!DOCTYPE html>
<html lang="en">
<head>
<meta charset="utf-8">
<title>Dana Morelbrat – Business Card</title>
<link rel="stylesheet" href="https://fonts.googleapis.com/css2?family=Arimo:wght@400;500&display=swap">
<style>
  :root {
    --yellow: #fcdc1c;
    --yellow-deep: #f8d30f;
    --yellow-soft: #f6d94a;
    --ink: #111111;
    --backdrop: #ecebe7;
    --wood-light: #b98a5a;
    --wood-dark: #6f4a2c;
    --photo-light: #9a9a9a;
    --photo-dark: #4e4e4e;
  }
  * { box-sizing: border-box; margin: 0; padding: 0; }
  html, body { width: 1200px; height: 914px; overflow: hidden; }
  body {
    background: var(--backdrop);
    font-family: "Arimo", Helvetica, Arial, sans-serif;
    color: var(--ink);
    display: flex;
    flex-direction: column;
    align-items: center;
    justify-content: center;
    gap: 40px;
  }
  .card {
    position: relative;
    width: 700px;
    height: 400px;
    overflow: hidden;
    box-shadow: 0 6px 18px rgba(0,0,0,.18);
  }

  /* Back side */
  .card-back { display: flex; }
  .services-panel {
    width: 406px;
    height: 100%;
    background: linear-gradient(160deg, var(--yellow-soft), var(--yellow-deep));
    padding: 42px 0 0 96px;
  }
  .services-title {
    display: flex;
    align-items: center;
    gap: 16px;
    font-size: 27px;
    font-weight: 400;
    letter-spacing: .5px;
    margin-bottom: 26px;
  }
  .services-title .plus { font-size: 36px; line-height: 1; font-weight: 500; }
  .service-list { list-style: none; }
  .service-item {
    display: flex;
    align-items: center;
    gap: 22px;
    height: 52px;
    font-size: 17px;
  }
  .service-icon {
    width: 38px; height: 38px;
    border-radius: 50%;
    background: #fff;
    display: flex; align-items: center; justify-content: center;
    flex-shrink: 0;
  }
  .service-icon svg { width: 22px; height: 22px; }
  .workspace-photo {
    flex: 1;
    background: radial-gradient(circle at 45% 55%, var(--wood-light), var(--wood-dark));
  }

  /* Front side */
  .card-front {
    background: linear-gradient(135deg, var(--yellow), var(--yellow-deep));
  }
  .holder-name {
    position: absolute;
    left: 150px; top: 52px;
    font-size: 31px;
    font-weight: 400;
    letter-spacing: .5px;
    text-transform: uppercase;
  }
  .contact-list {
    position: absolute;
    left: 66px; top: 112px;
    list-style: none;
  }
  .contact-item {
    display: flex;
    align-items: center;
    gap: 28px;
    height: 33px;
    font-size: 17px;
  }
  .contact-icon {
    width: 27px; height: 27px;
    border-radius: 7px;
    background: var(--ink);
    display: flex; align-items: center; justify-content: center;
    flex-shrink: 0;
  }
  .contact-icon svg { width: 17px; height: 17px; }
  .portrait {
    position: absolute;
    left: 420px; top: 150px;
    width: 240px; height: 210px;
    border: 4px solid var(--ink);
    background: radial-gradient(circle at 50% 60%, var(--photo-light), var(--photo-dark));
  }
</style>
</head>
<body>

<section class="card card-back">
  <div class="services-panel">
    <h2 class="services-title"><span class="plus">+</span>SERVICES</h2>
    <ul class="service-list">
      <li class="service-item">
        <span class="service-icon">
          <svg viewBox="0 0 24 24" fill="none" stroke="#111" stroke-width="1.6"><path d="M4 20l3-1 12-12-2-2L5 17z"/><path d="M15 7l2 2"/><path d="M4 4l16 16" stroke="#e8b400"/></svg>
        </span>Communications Strategy
      </li>
      <li class="service-item">
        <span class="service-icon">
          <svg viewBox="0 0 24 24" fill="none" stroke="#111" stroke-width="1.6"><rect x="6" y="3" width="12" height="7" fill="#fce27a"/><rect x="3" y="10" width="18" height="10" rx="2"/><path d="M7 14h10M7 17h10"/></svg>
        </span>Media Relations
      </li>
      <li class="service-item">
        <span class="service-icon">
          <svg viewBox="0 0 24 24" fill="none" stroke="#111" stroke-width="1.6"><path d="M3 7h7l2 2h9v10H3z" fill="#fce27a"/><path d="M6 12h12"/></svg>
        </span>PR &amp; Campaigns
      </li>
      <li class="service-item">
        <span class="service-icon">
          <svg viewBox="0 0 24 24" fill="none" stroke="#111" stroke-width="1.6"><path d="M12 3a6 6 0 0 0-3.5 10.9V16h7v-2.1A6 6 0 0 0 12 3z" fill="#fce27a"/><path d="M9.5 19h5M10.5 21.5h3"/></svg>
        </span>Strategic Counsel
      </li>
    </ul>
  </div>
  <div class="workspace-photo" role="img" aria-label="Overhead photo of a team working around a wooden table with laptops and notes"></div>
</section>

<section class="card card-front">
  <h1 class="holder-name">Dana Morelbrat</h1>
  <ul class="contact-list">
    <li class="contact-item">
      <span class="contact-icon">
        <svg viewBox="0 0 24 24" fill="#fff"><path d="M12 2a7 7 0 0 0-7 7c0 5 7 13 7 13s7-8 7-13a7 7 0 0 0-7-7zm0 9.5A2.5 2.5 0 1 1 12 6.5a2.5 2.5 0 0 1 0 5z"/></svg>
      </span>Sydney - Melbourne
    </li>
    <li class="contact-item">
      <span class="contact-icon">
        <svg viewBox="0 0 24 24" fill="none" stroke="#fff" stroke-width="2"><rect x="7" y="2" width="10" height="20" rx="2"/><path d="M10 18h4"/></svg>
      </span>0498 317 026
    </li>
    <li class="contact-item">
      <span class="contact-icon">
        <svg viewBox="0 0 24 24" fill="none" stroke="#fff" stroke-width="2"><rect x="3" y="5" width="18" height="14" rx="1"/><path d="M3 6l9 7 9-7"/></svg>
      </span>dana@morelbratton.example
    </li>
    <li class="contact-item">
      <span class="contact-icon"></span>danamorelbrat
    </li>
    <li class="contact-item">
      <span class="contact-icon">
        <svg viewBox="0 0 24 24" fill="none" stroke="#fff" stroke-width="2"><circle cx="12" cy="12" r="9"/><path d="M3 12h18M12 3c3 3 3 15 0 18M12 3c-3 3-3 15 0 18"/></svg>
      </span>morelbratton.example
    </li>
    <li class="contact-item">
      <span class="contact-icon"></span>@danamorelbrat
    </li>
  </ul>
  <div class="portrait" role="img" aria-label="Portrait photo of the consultant"></div>
</section>

</body>
</html>
```